Zielgruppe
Autor: Jura Professor
Zielgruppe: Digital- und Gesundheitswirtschaft
Foto des Autors in hoher Auflösung wird nachgereicht
Aufgabenstellung
Anlehnung an Vorschlag (siehe Word Dokument) wäre wünschenswert.
Aber auch völlig neue Vorschläge sind willkommen.
Bitte an dem Formatlayout im Anhang orientieren und Covers mit Vorder- und Rückseite sowie Buchrücken einsenden. Dankeschön.

```html
<!DOCTYPE html>
<html lang="de">
<head>
<meta charset="utf-8">
<title>Datenströme und Vernetzung im Kosmos der Justiz – Umschlag</title>
<link rel="stylesheet" href="https://fonts.googleapis.com/css2?family=Arimo:wght@400;500;600;700&family=Tinos:wght@400;700&display=swap">
<style>
  :root {
    --cover-blue: #1f4e7e;
    --page-bg: #eef0f2;
    --text-light: #ffffff;
    --image-deep: #0a2448;
    --image-mid: #1a6aa8;
    --image-glow: #6fd0f5;
  }
  * { margin: 0; padding: 0; box-sizing: border-box; }
  html, body { width: 931px; height: 1200px; overflow: hidden; background: var(--page-bg); }
  .spread {
    position: absolute; left: 0; top: 310px;
    width: 1000px; height: 622px;
    transform: scale(0.931); transform-origin: 0 0;
    background: var(--cover-blue); color: var(--text-light);
  }
  .back-cover { position: absolute; left: 0; top: 0; width: 480px; height: 622px; }
  .back-title { position: absolute; left: 51px; top: 48px; font: 600 15px/1.2 "Arimo", sans-serif; }
  .back-body { position: absolute; left: 51px; top: 78px; width: 415px; font: 700 6.4px/1.95 "Tinos", serif; }
  .back-body p { margin-bottom: 9px; }
  .back-body h3 { font: 600 9.5px/1.3 "Arimo", sans-serif; margin: 14px 0 4px; }
  .back-body ul { list-style: none; }
  .back-body li::before { content: "•  "; }
  .author-photo {
    position: absolute; left: 51px; top: 318px; width: 139px; height: 142px;
    border: 5px solid #fff;
    background: linear-gradient(160deg, #f2f2f2 0%, #d7dadd 55%, #3a3d42 100%);
  }
  .author-bio { position: absolute; left: 203px; top: 316px; width: 262px; font: 700 6.4px/1.95 "Tinos", serif; }
  .author-bio h3 { font: 600 9.5px/1.3 "Arimo", sans-serif; margin-bottom: 5px; }
  .author-bio ul { list-style: none; margin-top: 2px; }
  .author-bio li::before { content: "•   "; }
  .back-footer { position: absolute; left: 51px; top: 475px; width: 415px; font: 700 6.4px/1.95 "Tinos", serif; }
  .back-footer p { margin-bottom: 8px; }

  .spine { position: absolute; left: 480px; top: 0; width: 42px; height: 622px; }
  .spine-title, .spine-author {
    position: absolute; left: 21px; white-space: nowrap;
    transform: translate(-50%, -50%) rotate(-90deg);
  }
  .spine-title { top: 233px; font: 600 12.5px "Arimo", sans-serif; }
  .spine-author { top: 486px; font: 400 12px "Tinos", serif; }

  .front-cover { position: absolute; left: 522px; top: 0; width: 478px; height: 622px; }
  .image-strip { position: absolute; top: 0; height: 115px; background: linear-gradient(135deg, var(--image-deep), var(--image-mid) 60%, var(--image-glow)); }
  .strip-a { left: 3px; width: 150px; }
  .strip-b { left: 159px; width: 153px; background: radial-gradient(circle at 55% 45%, var(--image-glow), var(--image-mid) 35%, var(--image-deep) 80%); }
  .strip-c { left: 318px; width: 160px; background: linear-gradient(160deg, #cfe6f3, #4ea4d4 50%, #15538a); }
  .hero-image {
    position: absolute; left: 3px; top: 123px; width: 475px; height: 195px;
    background: radial-gradient(ellipse at 55% 50%, #a7e6fb 0%, #2f8fcf 30%, #0e3f73 65%, #061b36 100%);
  }
  .front-author { position: absolute; left: 45px; top: 368px; font: 400 15px "Tinos", serif; }
  .front-title { position: absolute; left: 45px; top: 412px; font: 600 28px/1.4 "Arimo", sans-serif; letter-spacing: 0.5px; }
  .front-subtitle { position: absolute; left: 45px; top: 497px; font: 400 15px/1.55 "Arimo", sans-serif; }
  .front-web { position: absolute; right: 29px; top: 591px; font: 400 9px "Tinos", serif; }
</style>
</head>
<body>
<div class="spread">
  <section class="back-cover">
    <h2 class="back-title">Datenströme und Vernetzung im Kosmos der Justiz</h2>
    <div class="back-body">
      <p>Einen einfachen Pfad durch den digitalen Wandel gibt es nicht. Wer in Unternehmen, Verwaltung oder Klinik Verantwortung trägt, sollte sich deshalb früh und gründlich mit den hier vorgestellten Leitlinien, Vorgehensweisen und konkreten Arbeitsschritten auseinandersetzen.<br>Der Band zeigt, dass vernetzte Prozesse und datengetriebene Angebote nur dann tragen, wenn ihre rechtlichen Voraussetzungen sorgfältig erarbeitet und verstanden werden.</p>
      <p>Ziel des Autors ist es, verlässliche Regeln im Umgang mit Daten zu stärken, vor allem im Gesundheitssektor.</p>
      <h3>Für wen das Buch geschrieben ist</h3>
      <ul>
        <li>Entscheider in Leitung und Management,</li>
        <li>Analysten, Controller, IT-Fachleute, Gesundheitsökonomen,</li>
        <li>Beauftragte für Regelkonformität und Datenschutz,</li>
        <li>Juristen und Fachanwälte,</li>
      </ul>
      <p>die sich fundiert mit den relevanten Rechtsfragen und neuen Themenfeldern der vernetzten Wirtschaft beschäftigen wollen.</p>
    </div>
    <div class="author-photo" role="img" aria-label="Porträtfoto des Herausgebers und Autors"></div>
    <div class="author-bio">
      <h3>Der Herausgeber und Autor</h3>
      <p>Prof. Dr. iur. Gottfried Halberg forscht und lehrt an Hochschulen in Berlin, Ludwigshafen/ Rhein, Stuttgart sowie an der Donauufer Universität Budapest. Er ist Professor, Visiting Professor und Dozent auf dem Gebiet der Rechtswissenschaften.</p>
      <p>Seine Forschungsschwerpunkte sowie zahlreiche Publikationen und Vorträge befassen sich insbesondere mit folgenden Themenfeldern:</p>
      <ul>
        <li>Vernetzung, Datenanalyse und Recht</li>
        <li>Datenschutz- und Datensicherheitsrecht</li>
        <li>Internetrecht, IuK-Recht</li>
        <li>Internationales Recht, Europa- und Wirtschaftsrecht</li>
      </ul>
    </div>
    <div class="back-footer">
      <p>Prof. Halberg verfügt über eine breite Projekt- und Gutachtenerfahrung sowie über ein umfangreiches internationales und nationales Netzwerk im Hochschulbereich und in der (Gesundheits-) Wirtschaft.</p>
      <p>Kontakt: gottfried@g-halberg.de; www.g-halberg.eu</p>
    </div>
  </section>

  <section class="spine">
    <span class="spine-title">Datenströme und Vernetzung im Kosmos der Justiz</span>
    <span class="spine-author">Gottfried Halberg</span>
  </section>

  <section class="front-cover">
    <div class="image-strip strip-a" role="img" aria-label="Leuchtende Weltkugel in digitalem Blau"></div>
    <div class="image-strip strip-b" role="img" aria-label="Digitaler Kopf aus Lichtdaten"></div>
    <div class="image-strip strip-c" role="img" aria-label="Roboterhand vor hellblauem Hintergrund"></div>
    <div class="hero-image" role="img" aria-label="Geschäftsmann berührt eine leuchtende Kugel aus Anwendungssymbolen mit Datenleitungen"></div>
    <p class="front-author">Gottfried Halberg (Hrsg. und Autor)</p>
    <h1 class="front-title">Datenströme und Vernetzung<br>im Kosmos der Justiz</h1>
    <p class="front-subtitle">Für eine verlässliche digitale Ordnung<br>im Gesundheitssektor</p>
    <p class="front-web">www.g-halberg.eu</p>
  </section>
</div>
</body>
</html>
```